Create an app design

Design a very simple travel app with the following specifications

Sign up/login page
- Username
- Phone number

Password code
- Type in 4 codes sent to your phone

Home page
- List of places friends have posted they're traveling to

Friends
- List of friends and where they're currently located
- Follow people by searching or adding from contact

Search
- Search for a specific country, state, or country and get a list of the people you follow who are there

```html
<!DOCTYPE html>
<html lang="en">
<head>
<meta charset="utf-8">
<title>Wanderly – App Screens</title>
<link href="https://fonts.googleapis.com/css2?family=Roboto:wght@400;500;700&display=swap" rel="stylesheet">
<style>
:root{
  --bg:#eaf3fb;
  --orange:#f2572a;
  --line:#f3b7a8;
  --dark-top:#303030;
  --dark-bottom:#1d1d1d;
  --white:#ffffff;
  --muted:#9a9a9a;
  --soft:#cfcfcf;
  --blue:#2d5fe3;
  --keypad:#d2d5db;
  --ink:#222222;
}
*{box-sizing:border-box;margin:0;padding:0}
html,body{width:1200px;height:2721px;overflow:hidden;background:var(--bg);font-family:'Roboto',sans-serif}
.board{position:relative;width:1200px;height:2721px}
.connectors{position:absolute;left:0;top:0}
.screen{position:absolute;width:345px;height:745px;border-radius:37px;overflow:hidden;
  background:linear-gradient(180deg,var(--dark-top),var(--dark-bottom));color:var(--white);
  box-shadow:0 18px 40px rgba(40,60,90,.12)}
.abs{position:absolute}
.home-bar{position:absolute;left:50%;bottom:12px;width:112px;height:4px;margin-left:-56px;border-radius:2px;background:var(--white)}
.home-bar.dark{background:var(--ink)}
.screen-title{position:absolute;top:23px;left:0;width:100%;text-align:center;font-size:13.5px;font-weight:500}
.back{position:absolute;top:22px;left:18px}
.btn{position:absolute;left:32px;width:280px;height:42px;border-radius:3px;background:var(--orange);
  color:var(--white);font-size:13px;font-weight:500;display:flex;align-items:center;justify-content:center}
.field{position:absolute;left:32px;width:280px;background:var(--white);border-radius:3px;color:var(--ink);display:flex;align-items:center;font-size:13px}
.field.active{border:2px solid var(--orange)}
.note{position:absolute;left:36px;width:273px;text-align:center;font-size:12.5px;line-height:24px;color:var(--muted)}
.app-name{font-family:'Roboto',sans-serif;font-weight:500;color:var(--white)}
.photo{position:absolute}
.slide{left:36px;top:659px;width:273px;height:41px;border-radius:21px;background:rgba(242,87,42,.55);display:flex;align-items:center}
.slide .knob{width:36px;height:36px;border-radius:50%;background:var(--orange);margin-left:2px;display:flex;align-items:center;justify-content:center}
.slide span{margin-left:36px;font-size:15px;font-weight:500;letter-spacing:1px}
.auth-btn{position:absolute;left:32px;width:280px;height:43px;border-radius:3px;display:flex;align-items:center;font-size:14px;font-weight:500;letter-spacing:1px}
.auth-btn .ico{width:20px;height:20px;border-radius:50%;background:var(--white);margin-left:28px;display:flex;align-items:center;justify-content:center}
.auth-btn .lbl{flex:1;text-align:center;margin-right:48px}
.code{position:absolute;top:233px;width:45px;height:43px;border-radius:3px;background:var(--white);color:var(--ink);font-size:19px;display:flex;align-items:center;justify-content:center}
.code.filled{border:2px solid var(--orange)}
.keypad{position:absolute;left:0;top:479px;width:345px;height:266px;background:var(--keypad)}
.key{position:absolute;width:108px;height:41px;background:var(--white);border-radius:5px;color:var(--ink);text-align:center;box-shadow:0 1px 0 #9aa0a8}
.key b{display:block;font-weight:400;font-size:19px;line-height:22px;margin-top:3px}
.key i{display:block;font-style:normal;font-size:7px;font-weight:700;letter-spacing:1.5px}
.avatar{position:absolute;left:116px;top:161px;width:112px;height:112px;border-radius:50%;background:radial-gradient(circle at 50% 40%,#8a6a55,#3e5d6e 70%);border:4px solid var(--white)}
.badge-plus{position:absolute;left:203px;top:253px;width:22px;height:22px;border-radius:50%;background:var(--orange);border:2px solid var(--white);color:var(--white);font-size:16px;line-height:17px;text-align:center}
.gender{position:absolute;left:32px;top:396px;width:280px;height:47px;background:var(--white);border-radius:3px;display:flex;align-items:center;padding:4px}
.gender .opt{height:39px;width:134px;border-radius:3px;display:flex;align-items:center;padding-left:18px;font-size:11px;color:var(--muted);gap:16px}
.gender .opt.on{background:var(--orange);color:var(--white)}
.feed{background:var(--white);color:var(--ink)}
.feed-head{position:absolute;left:0;top:0;width:345px;height:141px;background:linear-gradient(180deg,#2f2f2f,#1e1e1e);border-radius:0 0 14px 14px;color:var(--white)}
.search{position:absolute;left:17px;top:89px;width:311px;height:32px;background:var(--white);border-radius:2px;display:flex;align-items:center;font-size:10px;color:#c4c4c4}
.search .filter{position:absolute;right:0;top:0;width:32px;height:32px;background:var(--orange);display:flex;align-items:center;justify-content:center}
.section-title{position:absolute;left:16px;top:163px;font-size:13px;font-weight:500}
.suggest{position:absolute;top:191px;width:98px;height:131px;border-radius:3px;overflow:hidden;text-align:center;color:var(--white)}
.suggest .name{position:absolute;left:0;width:100%;top:92px;font-size:12px;font-weight:500}
.suggest .follow{position:absolute;left:23px;top:112px;width:52px;height:13px;border-radius:7px;background:var(--orange);font-size:7.5px;line-height:13px}
.poster{position:absolute;display:flex;align-items:center;gap:8px}
.poster .pic{width:28px;height:28px;border-radius:50%}
.poster .who{font-size:10px;line-height:13px}
.poster .who small{display:block;font-size:7.5px;color:var(--muted)}
.post{position:absolute;border-radius:3px;overflow:hidden}
.post .meta{position:absolute;left:10px;right:10px;bottom:6px;display:flex;justify-content:space-between;font-size:8px;color:var(--white)}
.nav{position:absolute;left:0;top:693px;width:345px;height:52px;background:var(--white);display:flex;justify-content:space-around;align-items:center;box-shadow:0 -2px 8px rgba(0,0,0,.06)}
.fab{position:absolute;left:158px;top:676px;width:34px;height:34px;border-radius:50%;background:var(--orange);border:3px solid var(--white);display:flex;align-items:center;justify-content:center}
.verified-title{position:absolute;top:481px;width:100%;text-align:center;font-size:20px;font-weight:500}
.verified-title em{font-style:normal;color:var(--orange)}
</style>
</head>
<body>
<div class="board">

  <svg class="connectors" width="1200" height="2721" viewBox="0 0 1200 2721" fill="none" stroke="#f3b7a8" stroke-width="5">
    <path d="M224 507 H178 Q151 507 151 534 V980"/>
    <path d="M569 507 H631"/>
    <path d="M366 1384 H428"/>
    <path d="M772 1384 H835"/>
    <path d="M1047 1725 V2270 Q1047 2307 1010 2307 H976"/>
    <path d="M569 2307 H631"/>
  </svg>

  <section class="screen intro" style="left:224px;top:104px">
    <div class="photo" role="img" aria-label="Photo of a traveller and her dog by a forest lake"
      style="inset:0;background:linear-gradient(180deg,#6b6f5c 0%,#46553c 28%,#3a3a2c 55%,#2d2a22 80%,#1f1c17 100%)"></div>
    <div class="abs slide">
      <div class="knob"><svg width="14" height="14" viewBox="0 0 14 14" fill="none" stroke="#fff" stroke-width="2" stroke-linecap="round"><path d="M2 7H12M8 3l4 4-4 4"/></svg></div>
      <span>Slide to explore</span>
    </div>
    <div class="home-bar"></div>
  </section>

  <section class="screen signin" style="left:631px;top:104px">
    <div class="photo" role="img" aria-label="Blurred photo of a forest lakeside"
      style="inset:0;background:linear-gradient(180deg,#4e5448 0%,#3c4236 35%,#3a2f26 60%,#1f1c19 100%)"></div>
    <div class="abs app-name" style="top:206px;width:100%;text-align:center;font-size:48px">Wanderly</div>
    <div class="abs" style="top:280px;width:100%;text-align:center;font-size:16px;font-weight:500;letter-spacing:1px;line-height:28px">Enhance your experience with<br><span style="color:var(--orange)">Wanderly.</span></div>
    <div class="abs" style="top:508px;width:100%;text-align:center;font-size:13.5px">Sign up or Log in with</div>
    <div class="auth-btn" style="top:541px;background:var(--blue)"><span class="ico"></span><span class="lbl">Linkbook</span></div>
    <div class="auth-btn" style="top:595px;background:var(--orange)">
      <span class="ico"><svg width="12" height="12" viewBox="0 0 24 24" fill="#f2572a"><path d="M6.6 10.8a15.1 15.1 0 006.6 6.6l2.2-2.2c.3-.3.7-.4 1-.2 1.1.4 2.3.6 3.6.6.6 0 1 .4 1 1V20c0 .6-.4 1-1 1A17 17 0 013 4c0-.6.4-1 1-1h3.5c.6 0 1 .4 1 1 0 1.3.2 2.5.6 3.6.1.3 0 .7-.2 1z"/></svg></span>
      <span class="lbl">Phone Number</span></div>
    <div class="abs" style="top:681px;width:100%;text-align:center;font-size:12.5px;color:#ddd">Continue without Sign in &nbsp;→</div>
    <div class="home-bar"></div>
  </section>

  <section class="screen phone-entry" style="left:21px;top:980px">
    <svg class="back" width="18" height="16" viewBox="0 0 18 16" fill="none" stroke="#fff" stroke-width="2" stroke-linecap="round"><path d="M16 8H2M8 2L2 8l6 6"/></svg>
    <div class="screen-title">Enter Your Phone Number</div>
    <div class="field active" style="top:177px;height:40px;padding-left:20px;font-weight:500;justify-content:space-between;padding-right:14px">Bangladesh
      <svg width="12" height="8" viewBox="0 0 12 8" fill="none" stroke="#f2572a" stroke-width="1.6"><path d="M1 1l5 5 5-5"/></svg></div>
    <div class="field" style="top:235px;height:41px">
      <span style="width:67px;text-align:center;color:var(--muted);border-right:1px solid #ddd;line-height:41px">+088</span>
      <span style="flex:1;text-align:center;color:#b8b8b8;font-size:11px">Phone Number</span></div>
    <div class="btn" style="top:312px">Send Verification Code</div>
    <p class="note" style="top:372px">We will send you a verify code to your phone number. Standard data charge may apply.</p>
    <div class="home-bar"></div>
  </section>

  <section class="screen verify" style="left:428px;top:980px">
    <svg class="back" width="18" height="16" viewBox="0 0 18 16" fill="none" stroke="#fff" stroke-width="2" stroke-linecap="round"><path d="M16 8H2M8 2L2 8l6 6"/></svg>
    <div class="screen-title">Phone Verification</div>
    <p class="abs" style="top:147px;width:100%;text-align:center;font-size:13.5px;line-height:23px;color:var(--soft)">A verification code is sent to your number<br>provided <span style="color:var(--white)">+0880000123456</span></p>
    <div class="code filled" style="left:41px">9</div>
    <div class="code filled" style="left:112px">7</div>
    <div class="code" style="left:184px"><span style="width:2px;height:20px;background:var(--orange)"></span></div>
    <div class="code" style="left:256px"></div>
    <div class="abs" style="top:286px;right:32px;font-size:11px;color:var(--orange)">Resend Code</div>
    <div class="btn" style="top:312px">Verify Number</div>
    <p class="note" style="top:372px;left:20px;width:305px;color:var(--soft)">By tapping verification number above, you agree to the <span style="color:var(--white)">Terms of Service, Privacy Policy</span> and <span style="color:var(--white)">Cookies Policy.</span></p>
    <div class="keypad">
      <div class="key" style="left:4px;top:5px"><b>1</b></div>
      <div class="key" style="left:118px;top:5px"><b>2</b><i>ABC</i></div>
      <div class="key" style="left:232px;top:5px"><b>3</b><i>DEF</i></div>
      <div class="key" style="left:4px;top:53px"><b>4</b><i>GHI</i></div>
      <div class="key" style="left:118px;top:53px"><b>5</b><i>JKL</i></div>
      <div class="key" style="left:232px;top:53px"><b>6</b><i>MNO</i></div>
      <div class="key" style="left:4px;top:103px"><b>7</b><i>PQRS</i></div>
      <div class="key" style="left:118px;top:103px"><b>8</b><i>TUV</i></div>
      <div class="key" style="left:232px;top:103px"><b>9</b><i>WXYZ</i></div>
      <div class="key" style="left:118px;top:151px"><b style="margin-top:9px">0</b></div>
      <svg class="abs" style="left:275px;top:164px" width="22" height="16" viewBox="0 0 22 16" fill="none" stroke="#222" stroke-width="1.4"><path d="M7 1h13v14H7L1 8z"/><path d="M11 5l6 6M17 5l-6 6"/></svg>
    </div>
    <div class="home-bar dark"></div>
  </section>

  <section class="screen profile" style="left:835px;top:980px">
    <div class="avatar" role="img" aria-label="Profile photo of the user"></div>
    <div class="badge-plus">+</div>
    <div class="field active" style="top:331px;height:45px;padding-left:18px;gap:14px;font-weight:500">
      <svg width="14" height="16" viewBox="0 0 14 16" fill="none" stroke="#999" stroke-width="1.3"><circle cx="7" cy="5" r="3.5"/><path d="M1 15c0-3.3 2.7-5.5 6-5.5s6 2.2 6 5.5"/></svg>Rafi Okan</div>
    <div class="gender">
      <div class="opt on"><svg width="14" height="14" viewBox="0 0 14 14" fill="none" stroke="#fff" stroke-width="1.3"><circle cx="5.5" cy="8.5" r="4"/><path d="M8.5 5.5L13 1M9 1h4v4"/></svg>Male</div>
      <div class="opt"><svg width="14" height="14" viewBox="0 0 14 14" fill="none" stroke="#999" stroke-width="1.3"><circle cx="5.5" cy="8.5" r="4"/><path d="M8.5 5.5L13 1M9 1h4v4"/></svg>Female</div>
    </div>
    <div class="field" style="top:461px;height:47px;padding-left:20px;gap:16px;color:var(--muted);font-size:11px">
      <svg width="12" height="16" viewBox="0 0 12 16" fill="none" stroke="#999" stroke-width="1.3"><path d="M6 15s5-5.2 5-9A5 5 0 001 6c0 3.8 5 9 5 9z"/><circle cx="6" cy="6" r="1.8"/></svg>Your Location</div>
    <div class="btn" style="top:634px">Update &amp; Finish</div>
    <div class="home-bar"></div>
  </section>

  <section class="screen feed" style="left:224px;top:1855px">
    <header class="feed-head">
      <div class="abs app-name" style="left:17px;top:22px;font-size:26px">Wanderly</div>
      <div class="search">
        <svg style="margin:0 14px 0 12px" width="16" height="16" viewBox="0 0 16 16" fill="none" stroke="#f2572a" stroke-width="1.6"><circle cx="7" cy="7" r="5"/><path d="M11 11l4 4"/></svg>
        Search for a specific country
        <div class="filter"><svg width="14" height="10" viewBox="0 0 14 10" stroke="#fff" stroke-width="1.4"><path d="M1 1h12M3 5h8M5 9h4"/></svg></div>
      </div>
    </header>
    <div class="section-title">Add to your feed</div>
    <div class="suggest" style="left:16px" role="img" aria-label="Portrait of suggested traveller"><div class="abs" style="inset:0;background:linear-gradient(180deg,#7d93a3,#50606b)"></div><div class="name">Mira Lenz</div><div class="follow">+ Follow</div></div>
    <div class="suggest" style="left:137px" role="img" aria-label="Portrait of suggested traveller"><div class="abs" style="inset:0;background:linear-gradient(180deg,#8a8474,#3d3a35)"></div><div class="name">Owen</div><div class="follow">+ Follow</div></div>
    <div class="suggest" style="left:258px" role="img" aria-label="Portrait of suggested traveller"><div class="abs" style="inset:0;background:linear-gradient(180deg,#4a6470,#26343b)"></div><div class="name">Tobias</div><div class="follow">+ Follow</div></div>

    <div class="poster" style="left:17px;top:357px"><div class="pic" style="background:#b88f7a"></div><div class="who">Mr. Harlow<small>Just Now</small></div></div>
    <div class="post" style="left:17px;top:387px;width:150px;height:168px" role="img" aria-label="Photo of an autumn forest">
      <div class="abs" style="inset:0;background:linear-gradient(180deg,#c9743a,#8a3d1d 60%,#4f2612)"></div>
      <div class="meta"><span>♡ 25</span><span>7 ◯</span></div></div>
    <div class="poster" style="left:17px;top:573px"><div class="pic" style="background:#7e8fb0"></div><div class="who">Mr. Harlow<small>3Min Ago</small></div></div>
    <div class="post" style="left:17px;top:609px;width:150px;height:84px" role="img" aria-label="Photo of snowy mountains">
      <div class="abs" style="inset:0;background:linear-gradient(180deg,#c9cdd0,#7d858b)"></div></div>

    <div class="poster" style="left:178px;top:357px"><div class="pic" style="background:#c07f6c"></div><div class="who">Mr. Harlow<small>2Min Ago</small></div></div>
    <div class="post" style="left:178px;top:387px;width:150px;height:116px" role="img" aria-label="Photo of a sea turtle underwater">
      <div class="abs" style="inset:0;background:linear-gradient(180deg,#3aa3d6,#1a6f9c)"></div>
      <div class="meta"><span>♡ 66</span><span>9 ◯</span></div></div>
    <div class="poster" style="left:178px;top:522px"><div class="pic" style="background:#5b4a40"></div><div class="who">Jonah Reyes<small>5Min Ago</small></div></div>
    <div class="post" style="left:178px;top:557px;width:150px;height:136px" role="img" aria-label="Photo of a turquoise mountain lake">
      <div class="abs" style="inset:0;background:linear-gradient(180deg,#8fa5b5,#5c7c8f 45%,#2fa3b8 75%,#1c7f95)"></div></div>

    <nav class="nav">
      <svg width="18" height="18" viewBox="0 0 18 18" fill="none" stroke="#f2572a" stroke-width="1.5"><path d="M2 8l7-6 7 6v8H2z"/><path d="M7 16v-5h4v5"/></svg>
      <svg width="18" height="18" viewBox="0 0 18 18" fill="none" stroke="#aaa" stroke-width="1.5"><path d="M2 3h14v10H6l-4 3z"/></svg>
      <span style="width:18px"></span>
      <svg width="18" height="18" viewBox="0 0 18 18" fill="none" stroke="#aaa" stroke-width="1.5"><path d="M4 13V8a5 5 0 0110 0v5l1.5 2h-13zM7 16h4"/><circle cx="14" cy="3" r="2" fill="#f2572a" stroke="none"/></svg>
      <svg width="18" height="18" viewBox="0 0 18 18" fill="none" stroke="#aaa" stroke-width="1.5"><circle cx="9" cy="9" r="7.5"/><circle cx="9" cy="7" r="2.5"/><path d="M4.5 14.5c1-2 2.6-3 4.5-3s3.5 1 4.5 3"/></svg>
    </nav>
    <div class="fab"><svg width="14" height="14" viewBox="0 0 14 14" stroke="#fff" stroke-width="2"><path d="M7 1v12M1 7h12"/></svg></div>
  </section>

  <section class="screen verified" style="left:631px;top:1855px">
    <div class="photo" role="img" aria-label="Illustration of a phone with a check mark and a person sitting beside it"
      style="left:56px;top:145px;width:233px;height:240px;border-radius:12px;background:radial-gradient(ellipse at 45% 50%,#5a5a5a 0%,#3a3a3a 55%,rgba(40,40,40,0) 75%)"></div>
    <div class="verified-title">Your phone number is <em>Verified!</em></div>
    <p class="note" style="top:526px;left:20px;width:305px">Lorem ipsum dolor sit amet, consectetur adipiscing elit. Eu elit at etiam turpis platea semper suscipit. Non est dis egestas duis sollicitudin sit nunc.</p>
    <div class="btn" style="top:636px">Complete Your Profile</div>
    <div class="home-bar"></div>
  </section>

</div>
</body>
</html>
```